Postcard for Antique Furniture Restorer

My business is to restore antique furniture. I am based in Sydney, Australia.

I will be using this postcard to promote my business.
I will give it to customers like a With Compliments card.

Sometimes I will be writing information on the back of the card.

Design for Postcard Size eg 148 X 105mm

Front of card:

Attached are images of Antique furniture - please use ONLY 1 of the 3 images.
Deep etch the image on a white or cream background.

On front of card add these words:
Timber Awakened
antique furniture restoration

Antiques travel through time, seeing generations of families
Through time they remain - they tell a continuing story
Be part of the journey

Back of postcard:
(leave space for notes to be handwritten)

Add these words:

Timber Awakened
Corwin Aldace
mobile 0437 552 681
www.oakmendworks.com.au

Industry/Entity Type

Business

Font styles to use
Serif
Sans Serif

Colors
fefdec
ffffff

Requirements
Must have
• Use only 1 image. Image must be deep etched.

```html
<!DOCTYPE html>
<html lang="en">
<head>
<meta charset="utf-8">
<title>Timber Awakened – Postcard</title>
<link rel="stylesheet" href="https://fonts.googleapis.com/css2?family=Philosopher:wght@400;700&family=Tinos:ital,wght@0,400;0,700;1,400;1,700&display=swap">
<style>
  :root{
    --stage:#3a3a3a;
    --cream:#fefdec;
    --cream-deep:#f1efdc;
    --white:#ffffff;
    --brown:#5a2410;
    --brown-soft:#6e3a22;
    --maroon:#5b1010;
    --timber-dark:#6b3a1c;
    --timber-light:#a0643a;
    --rule:#c9c4cf;
  }
  *{box-sizing:border-box;margin:0;padding:0}
  html,body{width:1200px;height:600px;overflow:hidden}
  body{background:var(--stage);position:relative;font-family:"Tinos",serif;color:var(--brown)}

  .card{position:absolute;top:110px;width:554px;height:394px;overflow:hidden;
    background:radial-gradient(ellipse at 50% 45%,var(--cream) 40%,var(--cream-deep) 100%)}
  .card--front{left:30px}
  .card--back{left:612px}

  .flourish-bg{position:absolute;inset:0;
    background:linear-gradient(135deg,rgba(230,226,205,.55),rgba(254,253,236,0) 45%,rgba(230,226,205,.5))}

  .timber-edge{position:absolute;background:linear-gradient(90deg,var(--timber-dark),var(--timber-light),var(--timber-dark))}
  .card--front .timber-edge{left:0;top:0;width:12px;height:100%}
  .card--back .timber-edge{left:0;bottom:0;width:100%;height:12px;
    background:linear-gradient(180deg,var(--timber-light),var(--timber-dark))}

  .intro-panel{position:absolute;left:28px;top:98px;width:440px;height:188px;
    background:rgba(254,253,236,.92);box-shadow:0 1px 4px rgba(0,0,0,.25);z-index:1}
  .intro-text{position:absolute;left:14px;top:10px;width:238px;text-align:center}
  .brand-name{font-family:"Philosopher",sans-serif;font-weight:700;font-size:24px;line-height:28px;color:var(--brown);white-space:nowrap}
  .brand-tag{font-family:"Tinos",serif;font-size:15px;line-height:18px;color:var(--brown);white-space:nowrap}
  .divider{display:block;width:40px;height:10px;margin:6px auto 6px;background:var(--brown-soft);border-radius:5px}
  .story{font-style:italic;font-size:12.5px;line-height:18px;color:var(--brown-soft);white-space:nowrap}
  .cta{font-family:"Philosopher",sans-serif;font-size:14px;margin-top:4px;color:var(--brown)}

  .armoire{position:absolute;left:280px;top:24px;width:242px;height:320px;z-index:2;
    background:linear-gradient(90deg,#4a1a0c,#8a3a1c 30%,#a44c24 50%,#7a2e14 75%,#4a1a0c)}

  .page-curl{position:absolute;right:0;bottom:0;width:110px;height:140px;z-index:3}

  .note-box{position:absolute;left:30px;top:24px;width:488px;height:216px;background:var(--white);
    border-radius:8px;box-shadow:0 1px 5px rgba(0,0,0,.25);padding-top:11px}
  .note-label{text-align:center;font-style:italic;font-weight:700;font-size:14px;color:var(--brown)}
  .note-lines{position:absolute;left:14px;right:14px;top:40px}
  .note-lines span{display:block;height:14px;border-bottom:1px solid var(--rule)}

  .contact{position:absolute;left:0;right:0;top:254px;text-align:center}
  .contact .brand-name{font-size:22px;line-height:26px}
  .contact .brand-tag{font-size:14.5px;color:var(--brown-soft)}
  .contact .divider{margin:5px auto 4px;width:34px;height:9px}
  .owner{font-style:italic;font-weight:700;font-size:17px;line-height:20px;color:var(--brown-soft)}
  .reach{font-size:14px;margin-top:4px;color:var(--brown)}
  .reach .phone{font-weight:700;font-size:16px}
</style>
</head>
<body>
  <section class="card card--front">
    <div class="flourish-bg" role="img" aria-label="Faint cream floral scroll pattern"></div>
    <div class="timber-edge" role="img" aria-label="Timber grain edge"></div>
    <div class="intro-panel">
      <div class="intro-text">
        <h1 class="brand-name">Timber Awakened</h1>
        <p class="brand-tag">Antique Furniture Restoration</p>
        <span class="divider" role="img" aria-label="Small flourish ornament"></span>
        <p class="story">Antiques travel through time, seeing<br>generations of families<br>Through time they remain - they tell a<br>continuing story</p>
        <p class="cta">Be part of the journey</p>
      </div>
    </div>
    <div class="armoire" role="img" aria-label="Deep-etched antique burl wood armoire with carved double doors"></div>
    <svg class="page-curl" viewBox="0 0 110 140" aria-hidden="true">
      <path d="M110 0 L110 140 L10 140 C40 110 80 60 110 0 Z" fill="var(--maroon)"/>
      <path d="M10 140 C30 128 42 120 48 104 C30 112 18 124 10 140 Z" fill="#f4f2ea" stroke="#d8d4c4"/>
      <path d="M64 108 L74 120 L64 132 M76 108 L86 120 L76 132" fill="none" stroke="var(--white)" stroke-width="3"/>
    </svg>
  </section>

  <section class="card card--back">
    <div class="flourish-bg" role="img" aria-label="Faint cream floral scroll pattern"></div>
    <div class="note-box">
      <p class="note-label">Note:</p>
      <div class="note-lines">
        <span></span><span></span><span></span><span></span><span></span><span></span>
        <span></span><span></span><span></span><span></span><span></span><span></span>
      </div>
    </div>
    <div class="contact">
      <h2 class="brand-name">Timber Awakened</h2>
      <p class="brand-tag">Antique Furniture Restoration</p>
      <span class="divider" role="img" aria-label="Small flourish ornament"></span>
      <p class="owner">Corwin Aldace</p>
      <p class="reach"><span class="phone">0437 552 681</span> &bull; www.oakmendworks.com.au</p>
    </div>
    <div class="timber-edge" role="img" aria-label="Timber grain edge"></div>
  </section>
</body>
</html>
```